The Wellness Barn Business Card

Info for the front..... (in whichever order and layout looks best)
Carla Penhallow
Physiotherapist
4/37 Upper Creekbank Rd
Tallowbrook
QLD 4712
0462305178
carlapenhallow57@mailbox.example
www.thewellnessbarn.example.au
on the back I would like to be able to write appointments so probably just that heading with lines.
I like a sort of rustic style but mostly professional, colours in naturals, beige, brown, green etc. I dont mind if the logo colour is changed slightly to suit.

```html
<!DOCTYPE html>
<html lang="en">
<head>
<meta charset="utf-8">
<title>The Wellness Barn Business Card</title>
<link rel="stylesheet" href="https://fonts.googleapis.com/css2?family=Open+Sans:wght@400;700&display=swap">
<style>
  :root {
    --backdrop: #d9d9d6;
    --brand-green: #2c4f1c;
    --brand-green-deep: #24421a;
    --ink: #3a3a3a;
    --paper: #ffffff;
  }
  * { box-sizing: border-box; margin: 0; padding: 0; }
  html, body {
    width: 1200px; height: 939px; overflow: hidden;
    background: var(--backdrop);
    font-family: "Open Sans", sans-serif;
  }
  .sheet {
    width: 1200px; height: 939px;
    display: flex; flex-direction: column; align-items: center; justify-content: center;
    gap: 40px;
  }
  .card {
    width: 660px; height: 378px;
    position: relative;
    box-shadow: 0 6px 18px rgba(0,0,0,.25);
  }
  .card--back {
    background: var(--brand-green);
    display: flex; align-items: center; justify-content: center;
  }
  .back-brand {
    font-weight: 700; font-size: 46px; line-height: 1.05;
    color: var(--brand-green-deep); text-align: center;
  }
  .card--front { background: var(--paper); }
  .front-brand {
    position: absolute; left: 40px; top: 88px; width: 230px;
    font-weight: 700; font-size: 44px; line-height: 1.05;
    color: var(--brand-green); text-align: center;
  }
  .divider {
    position: absolute; left: 300px; top: 44px;
    width: 1.5px; height: 200px; background: var(--ink);
  }
  .contact { position: absolute; left: 326px; top: 36px; color: var(--ink); }
  .contact__name {
    font-weight: 700; font-size: 27px; color: var(--brand-green); line-height: 1.1;
  }
  .contact__role, .contact__address {
    font-size: 13.5px; line-height: 1.55; padding-left: 26px;
  }
  .contact__address { padding-left: 50px; }
  .contact__list { list-style: none; margin-top: 6px; padding-left: 40px; }
  .contact__list li {
    font-size: 13.5px; line-height: 1.6; display: flex; align-items: center; gap: 6px;
    letter-spacing: .3px;
  }
  .contact__list svg { width: 12px; height: 12px; fill: var(--brand-green); flex: none; }
  .appointments {
    position: absolute; left: 30px; right: 30px; bottom: 30px;
    display: flex; align-items: baseline; gap: 6px;
    font-weight: 700; font-size: 15px; color: var(--brand-green);
  }
  .appointments .fill {
    border-bottom: 2px dotted var(--ink); height: 1px;
  }
  .fill--long { flex: 2.2; }
  .fill--mid { flex: 1.2; }
  .fill--short { flex: 1; }
</style>
</head>
<body>
<main class="sheet">
  <section class="card card--back" aria-label="Card back">
    <div class="back-brand">The Wellness<br>Barn</div>
  </section>

  <section class="card card--front" aria-label="Card front">
    <div class="front-brand">The Wellness Barn</div>
    <div class="divider"></div>
    <div class="contact">
      <p class="contact__name">Carla Penhallow</p>
      <p class="contact__role">Physiotherapist</p>
      <p class="contact__address">4/37 Upper Creekbank Rd<br>Tallowbrook<br>QLD 4712</p>
      <ul class="contact__list">
        <li>
          <svg viewBox="0 0 24 24" aria-hidden="true"><path d="M6.6 10.8a15.1 15.1 0 0 0 6.6 6.6l2.2-2.2a1 1 0 0 1 1-.25 11.4 11.4 0 0 0 3.6.57 1 1 0 0 1 1 1V20a1 1 0 0 1-1 1A17 17 0 0 1 3 4a1 1 0 0 1 1-1h3.5a1 1 0 0 1 1 1c0 1.25.2 2.45.57 3.57a1 1 0 0 1-.25 1z"/></svg>
          0462305178
        </li>
        <li>
          <svg viewBox="0 0 24 24" aria-hidden="true"><path d="M2 5h20v14H2z M2 5l10 8 10-8" fill="none" stroke="#2c4f1c" stroke-width="2.5"/></svg>
          carlapenhallow57@mailbox.example
        </li>
        <li>
          <svg viewBox="0 0 24 24" aria-hidden="true"><circle cx="12" cy="12" r="10" fill="none" stroke="#2c4f1c" stroke-width="2.5"/><path d="M2 12h20M12 2c3 3 3 17 0 20M12 2c-3 3-3 17 0 20" fill="none" stroke="#2c4f1c" stroke-width="2"/></svg>
          www.thewellnessbarn.example.au
        </li>
      </ul>
    </div>
    <div class="appointments">
      <span>Appointments:</span><span class="fill fill--long"></span>
      <span>Date:</span><span class="fill fill--mid"></span>
      <span>Time:</span><span class="fill fill--short"></span>
    </div>
  </section>
</main>
</body>
</html>
```